Hispanic Financial Counseling and Advocate Firm seeks business card design

Looking for a clean, professional business card design. This is a firm that specializes in providing financial education, coaching, and planning to the Hispanic community. The name of the company is Valemar, which means to prosper. We need a design that is clean, professional, and invokes trust, professionalism, but also welcoming. Our logo is a plant growing from a hand to give the messaging of of being in control of growing your financial future and security. Its part of a larger organization names Celesta Financial Group, who's logo is a tree with multi colored branches. We have the back of the card designed so we just need the front designed. the back is blue, so front needs to be a different background color, not blue.

Target Market(s)

Hispanic Community looking to better their future

Industry/Entity Type

financial services

Contact Information for Business Card

contact info: Anselmo Ibarra Jr, 951-555-0147, info@celestafinancialgroup.example. Celestafinancialgroup.example. tag line: Para un futuro mas seguro!

Requirements
Must have
• basics: logo, contact info.
Nice to have
• possibly incorporate the tree logo provided somehow
Should not have
• should not look like the back, needs to be different from the back provided.

```html
<!DOCTYPE html>
<html lang="es">
<head>
<meta charset="utf-8">
<title>Celesta Financial Group – Business Card Front</title>
<link rel="stylesheet" href="https://fonts.googleapis.com/css2?family=Source+Sans+3:wght@400;600;700&display=swap">
<style>
  :root {
    --backdrop: #e4e5e7;
    --card: #f7f7f5;
    --sky: #1a9ed9;
    --navy: #0f3b57;
    --red: #d9414a;
    --green: #94c23c;
    --yellow: #f2c21b;
    --purple: #a47fbf;
    --teal: #17a6c9;
  }
  * { box-sizing: border-box; margin: 0; padding: 0; }
  html, body {
    width: 1200px;
    height: 1200px;
    overflow: hidden;
    background: var(--backdrop);
    font-family: "Source Sans 3", "Myriad Pro", Arial, sans-serif;
  }
  .card {
    position: absolute;
    left: 75px;
    top: 300px;
    width: 1050px;
    height: 600px;
    background: var(--card);
    overflow: hidden;
    box-shadow: 0 10px 30px rgba(0,0,0,0.12);
  }
  .band-top {
    position: absolute; left: 0; top: 0;
    width: 100%; height: 14px;
    background: var(--sky);
  }
  .band-bottom {
    position: absolute; left: 0; bottom: 12px;
    width: 100%; height: 16px;
    background: var(--navy);
  }
  .tab { position: absolute; width: 50px; height: 78px; }
  .tab-red    { left: 0;  top: 58px;  background: var(--red); }
  .tab-green  { left: 0;  top: 205px; background: var(--green); }
  .tab-yellow { right: 0; top: 228px; background: var(--yellow); }
  .tab-purple { right: 0; top: 400px; background: var(--purple); }

  .brand {
    position: absolute;
    left: 90px; top: 200px;
    width: 320px;
    display: flex; flex-direction: column; align-items: center; gap: 18px;
  }
  .brand-mark {
    width: 34px; height: 34px;
    background: var(--navy);
  }
  .brand-name {
    font-weight: 700;
    font-size: 30px;
    line-height: 1.15;
    text-align: center;
    color: var(--navy);
  }

  .divider {
    position: absolute;
    left: 450px; top: 92px;
    width: 2px; height: 390px;
    background: var(--red);
  }
  .details {
    position: absolute;
    left: 500px; top: 100px;
    color: var(--navy);
  }
  .person-name {
    font-weight: 700;
    font-size: 38px;
    line-height: 1.1;
  }
  .person-title {
    font-size: 22px;
    color: var(--teal);
    margin-top: 2px;
  }
  .contact {
    list-style: none;
    margin-top: 58px;
    font-size: 26px;
    line-height: 1.3;
  }
  .tagline {
    margin-top: 34px;
    font-size: 25px;
    color: var(--red);
  }
</style>
</head>
<body>
  <main class="card">
    <div class="band-top"></div>
    <div class="tab tab-red"></div>
    <div class="tab tab-green"></div>
    <div class="tab tab-yellow"></div>
    <div class="tab tab-purple"></div>

    <div class="brand">
      <span class="brand-mark"></span>
      <span class="brand-name">Celesta Financial Group</span>
    </div>

    <div class="divider"></div>

    <section class="details">
      <h1 class="person-name">Anselmo Ibarra Jr</h1>
      <p class="person-title">CEO</p>
      <ul class="contact">
        <li>951-555-0147</li>
        <li>info@celestafinancialgroup.example</li>
        <li>Celestafinancialgroup.example</li>
      </ul>
      <p class="tagline">Para un futuro mas seguro!</p>
    </section>

    <div class="band-bottom"></div>
  </main>
</body>
</html>
```